Webdesign für  FAQ-Finder
Webdesign für FAQ-Finder
Zielgruppe
wiego-lumi.de ist ein FAQ-Finder für werdende / frisch gebackene Eltern in einem ansprechenden, effizienten und modernen Design.
Aufgabenstellung
Ein mobile first Designansatz basierenden auf einem cleanen, modernen Interface und Illustrationen im Stile von:
https://pixelkorb.example/shots/20581934-Tervon-a-fund-for-many
Es gibt noch kein Logo und kein CI. Die Farbwelt soll sich an dem Beispiel von
https://www.quarnetpantry.example/collections
orientieren. Gedeckt, warm. Thematisch geht es um Babies.
For structure perhaps like this:
https://pixelkorb.example/shots/20947715-Flexible-layout-for-Sitewerk-theming-service/attachments/7310452?mode=media
https://pixelkorb.example/shots/20633179--Staffing-Role-locator-Query-App
For Content:
https://www.wiegenpfad.example/category/themen/baby/

```html
<!DOCTYPE html>
<html lang="de">
<head>
<meta charset="utf-8">
<title>wiego-lumi.de – Unsere Themen</title>
<link href="https://fonts.googleapis.com/css2?family=Poppins:wght@300;400;500;600;700;800&display=swap" rel="stylesheet">
<style>
:root{
  --ink:#111118;
  --muted:#a4a4ad;
  --purple:#5a48c0;
  --purple-soft:#b9afe8;
  --lavender:#f5f4fc;
  --line:#dedde4;
  --mint:#4fc3a0;
  --mint-soft:#bfe6d8;
  --white:#ffffff;
}
*{box-sizing:border-box;margin:0;padding:0}
html,body{width:726px;height:1200px;overflow:hidden;background:var(--white)}
body{position:relative;font-family:'Poppins',sans-serif;color:var(--ink)}
.abs{position:absolute}
.brand{display:flex;flex-direction:column;align-items:center;gap:3px}
.brand-dot{width:26px;height:26px;border-radius:50%;border:2px solid var(--purple)}
.brand-name{font-size:12px;font-weight:400;color:var(--ink);letter-spacing:-.2px}
.nav{top:22px;left:385px;display:flex;gap:0;font-size:9px}
.nav a{color:var(--ink);text-decoration:none;margin-right:17px;padding:2px 2px;white-space:nowrap}
.nav a.active{border-bottom:1px solid var(--purple)}
.nav .caret{font-size:6px;margin-left:2px}
.hero-title{left:126px;top:132px;font-size:21px;font-weight:800;line-height:24.5px;letter-spacing:.6px}
.hero-text{left:126px;top:188px;width:220px;font-size:8.3px;line-height:13.6px;color:var(--muted);font-weight:300}
.hero-art{left:407px;top:72px;width:186px;height:218px;border-radius:48% 52% 40% 60% / 40% 38% 62% 60%;
  background:radial-gradient(circle at 55% 50%,var(--mint) 0 22%,var(--mint-soft) 40%,var(--lavender) 70%)}
.search{left:215px;top:322px;width:315px;height:30px;border-radius:14px;background:var(--lavender);
  font-size:8px;color:#8a8a94;padding:0 9px;display:flex;align-items:center;justify-content:space-between}
.topic{width:110px;text-align:center}
.topic-tile{width:70px;height:70px;margin:0 auto;border-radius:24px;background:var(--white);
  box-shadow:0 6px 16px rgba(90,72,192,.08);display:flex;align-items:center;justify-content:center}
.topic-icon{width:28px;height:30px;border-radius:9px;background:var(--lavender);border:2px solid var(--purple-soft)}
.topic-label{margin-top:14px;font-size:9.3px;font-weight:600;letter-spacing:.7px}
.top-box{left:90px;top:664px;width:546px;height:276px;border:1px solid var(--line);border-radius:30px;padding:20px 23px}
.top-box h2{font-size:17px;font-weight:700;margin-bottom:8px}
.faq-list{list-style:none}
.faq-list li{font-size:8.4px;font-weight:500;height:22.7px;display:flex;align-items:center;border-bottom:1px solid var(--line)}
.faq-list li:last-child{border-bottom:none}
.btn{display:inline-block;background:var(--purple);color:var(--white);font-size:7.5px;font-weight:500;
  border-radius:10px;padding:0 14px;height:19px;line-height:19px;margin-top:8px}
.footer-rule{left:0;top:984px;width:726px;height:2px;background:var(--purple)}
.address{left:90px;top:1058px;font-size:7.6px;line-height:16.4px}
.f-head{font-size:10px;font-weight:500}
.f-links{list-style:none;font-size:7.8px;line-height:15px;margin-top:6px;padding-left:1px}
.news-text{font-size:7.3px;line-height:13.6px;margin-top:7px;width:192px}
.news-form{display:flex;gap:6px;margin-top:10px}
.news-input{width:112px;height:21px;border-radius:10px;background:var(--lavender);font-size:6.5px;color:#8a8a94;padding:0 10px;line-height:21px}
.news-btn{width:67px;height:21px;border-radius:10px;background:var(--purple);color:var(--white);font-size:8px;text-align:center;line-height:21px}
.socials{display:flex;gap:12px;margin-top:13px;padding-left:2px}
.socials span{width:8px;height:8px;border-radius:50%;background:var(--purple-soft)}
.foot-rule{left:70px;top:1163px;width:545px;height:1px;background:var(--line)}
.copyright{left:0;top:1177px;width:686px;text-align:center;font-size:7.3px}
</style>
</head>
<body>
<header>
  <div class="abs brand" style="left:90px;top:12px">
    <span class="brand-dot"></span>
    <span class="brand-name">wiego-lumi.de</span>
  </div>
  <nav class="abs nav">
    <a class="active">Home</a>
    <a>über uns</a>
    <a>Themen<span class="caret">⌄</span></a>
    <a>Tipps &amp; Tools</a>
    <a>Kontakt</a>
  </nav>
</header>

<main>
  <h1 class="abs hero-title">UNSERE THEMEN<br>FÜR SIE</h1>
  <p class="abs hero-text">Hier finden Sie alle Themen rund um das Baby, die Geburtsvorbereitung, Schwangerschaft, Stillen, den Kinderwunsch und das Familienleben.</p>
  <div class="abs hero-art" role="img" aria-label="Illustration: Mutter hält ihr Baby im Arm, umgeben von Blättern"></div>

  <div class="abs search">
    <span>Suche ...</span>
    <svg width="15" height="15" viewBox="0 0 15 15" fill="none" stroke="#111118" stroke-width="1.3"><circle cx="7" cy="7" r="5.6"/><path d="M11 11l3 3"/></svg>
  </div>

  <section class="abs" style="left:88px;top:387px;display:flex;gap:0">
    <div class="topic"><div class="topic-tile"><span class="topic-icon" role="img" aria-label="Symbol Kinderwunsch"></span></div><div class="topic-label">Kinderwunsch</div></div>
    <div class="topic"><div class="topic-tile"><span class="topic-icon" role="img" aria-label="Symbol Schwangerschaft"></span></div><div class="topic-label">Schwangerschaft</div></div>
    <div class="topic"><div class="topic-tile"><span class="topic-icon" role="img" aria-label="Symbol Geburt"></span></div><div class="topic-label">Geburt</div></div>
    <div class="topic"><div class="topic-tile"><span class="topic-icon" role="img" aria-label="Symbol Stillen"></span></div><div class="topic-label">Stillen</div></div>
    <div class="topic"><div class="topic-tile"><span class="topic-icon" role="img" aria-label="Symbol Kleinkind"></span></div><div class="topic-label">Kleinkind</div></div>
  </section>
  <section class="abs" style="left:88px;top:514px;display:flex;gap:0">
    <div class="topic"><div class="topic-tile"><span class="topic-icon" role="img" aria-label="Symbol Kinderwunsch"></span></div><div class="topic-label">Kinderwunsch</div></div>
    <div class="topic"><div class="topic-tile"><span class="topic-icon" role="img" aria-label="Symbol Schwangerschaft"></span></div><div class="topic-label">Schwangerschaft</div></div>
    <div class="topic"><div class="topic-tile"><span class="topic-icon" role="img" aria-label="Symbol Geburt"></span></div><div class="topic-label">Geburt</div></div>
    <div class="topic"><div class="topic-tile"><span class="topic-icon" role="img" aria-label="Symbol Stillen"></span></div><div class="topic-label">Stillen</div></div>
    <div class="topic"><div class="topic-tile"><span class="topic-icon" role="img" aria-label="Symbol Kleinkind"></span></div><div class="topic-label">Kleinkind</div></div>
  </section>

  <section class="abs top-box">
    <h2>Top angesehen</h2>
    <ul class="faq-list">
      <li>Woran merke ich, dass meinem Baby kalt ist?</li>
      <li>Consectetur adipiscing elit Donec non mollis arcu. Integer ultricies gravida dolor?</li>
      <li>Vestibulum et diam eu diam sollicitudin porta Integer at leo sit amet lorem imperdiet?</li>
      <li>Nunc vel lorem eu enim scelerisque semper a sit amet ex Proin luctus tempus ligula eget tristique?</li>
      <li>Nam feugiat eu mi sed tincidunt Nunc quis euismod nisi?</li>
      <li>Quisque dapibus in lorem luctus faucibus. Curabitur non quam ultrices?</li>
      <li>Mauris viverra purus ac justo vestibulum viverra sed et quam?</li>
      <li>Nullam sit amet ipsum ipsum. Fusce massa dolor vehicula accumsan volutpat vel?</li>
    </ul>
    <span class="btn">mehr sehen</span>
  </section>
</main>

<footer>
  <div class="abs footer-rule"></div>
  <div class="abs brand" style="left:90px;top:1005px">
    <span class="brand-dot"></span>
    <span class="brand-name">wiego-lumi.de</span>
  </div>
  <address class="abs address" style="font-style:normal">
    Lindenhofweg 14 Mannheim<br>Baden-Württemberg<br>(+49)-800-5172-40<br>info@wiegenpfad-hilfe.example<br>wiegenpfad-hilfe.example
  </address>
  <div class="abs" style="left:258px;top:1032px">
    <div class="f-head">Information</div>
    <ul class="f-links"><li>Home</li><li>Über uns</li><li>Themen</li><li>Tipps &amp; Tools</li><li>Kontakt</li><li>Impressum</li></ul>
  </div>
  <div class="abs" style="left:425px;top:1032px">
    <div class="f-head">Newsletter</div>
    <p class="news-text">Lorem ipsum dolor sit amet, consecte adipiscing elit. Maecenas quis viverra felis nec mattis mauris.</p>
    <div class="news-form"><span class="news-input">E-Mail</span><span class="news-btn">Abonnieren</span></div>
    <div class="socials"><span></span><span></span><span></span><span></span><span></span></div>
  </div>
  <div class="abs foot-rule"></div>
  <div class="abs copyright">© 2021 wiego-lumi.de Alle Rechte vorbehalten</div>
</footer>
</body>
</html>
```